banner add for tamrick sports bar and grill

need an eye catching banner design that will atract passing cars .
size will be 8 feet tall by 16feet wide

serving breakfst, lunch and dinner

best place for all PPV events

pastas,wings , ribs , gourmet burgers , salads , steaks , mexican food and seafood

phone number 418 3367

facebook/tamricksportsbar

open from 7:00AM

Industry/Entity Type

Sports Bar

```html
<!DOCTYPE html>
<html lang="en">
<head>
<meta charset="utf-8">
<title>Tamrick Sports Bar &amp; Grill – Banner</title>
<link rel="stylesheet" href="https://fonts.googleapis.com/css2?family=Russo+One&family=Arimo:wght@700&display=swap">
<style>
  :root {
    --page-bg: #eeeeee;
    --page-glow: #fbfbf3;
    --banner-red: #e8202a;
    --banner-orange: #e8682a;
    --band-black: #0c0c0c;
    --accent-yellow: #ece31a;
    --ink-dark: #2a2a2a;
    --brand-red: #c61f2a;
    --white: #ffffff;
  }
  * { margin: 0; padding: 0; box-sizing: border-box; }
  html, body { width: 1200px; height: 1000px; overflow: hidden; }
  body {
    background: radial-gradient(ellipse at 50% 48%, var(--page-glow) 0%, var(--page-bg) 70%);
    font-family: "Arimo", Arial, sans-serif;
    position: relative;
  }
  .banner {
    position: absolute;
    left: 65px; top: 228px;
    width: 1073px; height: 537px;
    background: linear-gradient(90deg, var(--banner-red) 0%, var(--banner-orange) 45%, var(--banner-orange) 55%, var(--banner-red) 100%);
    box-shadow: 4px 5px 8px rgba(0,0,0,0.35);
    overflow: hidden;
  }
  .brand-badge {
    position: absolute;
    left: 65px; top: 60px;
    width: 370px; height: 370px;
    border-radius: 50%;
    background: var(--white);
    display: flex; flex-direction: column;
    align-items: center; justify-content: center;
    color: var(--brand-red);
    font-family: "Arimo", Arial, sans-serif;
    font-weight: 700;
    text-align: center;
    line-height: 1.05;
  }
  .brand-badge .name-main { font-size: 64px; }
  .brand-badge .name-sub { font-size: 34px; margin-top: 10px; }
  .headline {
    position: absolute;
    left: 490px; top: 46px;
    width: 570px;
    text-align: center;
    color: var(--white);
    font-family: "Russo One", "Arial Black", sans-serif;
    font-size: 64px;
    line-height: 82px;
    letter-spacing: 2px;
  }
  .hours {
    position: absolute;
    left: 560px; top: 282px;
    width: 470px;
    text-align: center;
    color: var(--white);
    font-weight: 700;
    font-size: 20px;
    line-height: 25px;
  }
  .contact-box {
    position: absolute;
    left: 621px; top: 365px;
    width: 452px; height: 97px;
    background: var(--accent-yellow);
    color: var(--ink-dark);
  }
  .contact-box .phone-icon {
    position: absolute; left: 46px; top: 20px;
    width: 44px; height: 60px;
  }
  .contact-box .phone-number {
    position: absolute; left: 117px; top: 6px;
    font-size: 52px; letter-spacing: 1px;
  }
  .contact-box .social-handle {
    position: absolute; left: 118px; top: 64px;
    font-size: 19px;
  }
  .menu-band {
    position: absolute;
    left: 0; bottom: 0;
    width: 100%; height: 60px;
    background: var(--band-black);
    color: var(--white);
    font-size: 19px;
    letter-spacing: 0.5px;
    display: flex; align-items: center; justify-content: center;
  }
</style>
</head>
<body>
  <section class="banner">
    <div class="brand-badge">
      <span class="name-main">Tamrick</span>
      <span class="name-sub">Sports Bar &amp; Grill</span>
    </div>

    <h1 class="headline">BEST PLACE<br>FOR ALL<br>PPV EVENTS</h1>

    <p class="hours">open from 7:00AM<br>serve breakfast, lunch and dinner</p>

    <div class="contact-box">
      <svg class="phone-icon" viewBox="0 0 44 60" aria-hidden="true">
        <path fill="#2a2a2a" d="M10 2 L18 2 L21 16 L15 20 C15 28 18 36 24 42 L30 38 L40 46 L38 54 C34 58 28 60 22 56 C10 46 3 30 4 14 C4 8 6 4 10 2 Z"/>
      </svg>
      <span class="phone-number">418 3367</span>
      <span class="social-handle">facebook/tamricksportsbar</span>
    </div>

    <div class="menu-band">PASTAS,WINGS , RIBS , GOURMET BURGERS , SALADS , STEAKS , MEXICAN FOOD AND SEAFOOD</div>
  </section>
</body>
</html>
```